Animal Hospital Business Cards

Make a business card look like the attached example

*Use the same blue/black coloring
*Fenbrook Hollow Animal Hospital (instead of mobile pet rounds)
*Emergency Services (instead of tri-county care center)
*House Calls (instead of open 7 days by appointment)
*Change address to 1873 Tilden Marsh Rd Loveland, OH 45140
*Open 7 days a week (instead of emergency service)
*Add the website www.fenbrookhollowanimalhospital.example

On the back...
*instead of the text outlined in red, just white
*instead of the light blue, try your best to make it just like the blue and black on the front side of the card
*Delete "designed and printed by Blue Heron Print Co, www.blueheronprintco.example

Requirements
Must have
• look just like the attached example with requested edits/changes

```html
<!DOCTYPE html>
<html lang="en">
<head>
<meta charset="utf-8">
<title>Fenbrook Hollow Animal Hospital – Business Card</title>
<link href="https://fonts.googleapis.com/css2?family=Open+Sans:wght@700&family=Roboto+Condensed:wght@400;700&family=Lato:wght@400&family=Tinos:wght@400;700&display=swap" rel="stylesheet">
<style>
  :root {
    --teal: #1b4a5c;
    --black: #111111;
    --white: #ffffff;
    --ink: #111111;
    --grey: #555555;
    --stage: #ece7e1;
  }
  * { margin: 0; padding: 0; box-sizing: border-box; }
  html, body { width: 1200px; height: 900px; overflow: hidden; }
  body { background: var(--stage); position: relative; }

  .card {
    position: absolute;
    background: var(--white);
    box-shadow: 2px 3px 6px rgba(0,0,0,0.35);
    overflow: hidden;
  }
  .card-front { left: 330px; top: 90px; width: 555px; height: 343px; }
  .card-back  { left: 330px; top: 470px; width: 559px; height: 343px; }

  .bands { position: absolute; inset: 0; }
  .txt { position: absolute; white-space: nowrap; line-height: 1; }
  .center { transform: translateX(-50%); }

  .hospital-name {
    left: 277px; top: 29px;
    font: 700 24px "Open Sans", sans-serif; color: var(--white);
  }
  .vet-name {
    left: 277px; top: 108px;
    font: 700 21px "Tinos", serif; color: var(--ink);
  }
  .website {
    left: 277px; top: 140px;
    font: 400 16px "Roboto Condensed", sans-serif; color: var(--ink);
  }
  .service-left {
    left: 25px; top: 174px;
    font: 400 18px "Open Sans", sans-serif; font-weight: 400; color: var(--ink);
    line-height: 22px; white-space: normal; width: 110px;
    font-family: "Lato", sans-serif;
  }
  .species {
    left: 276px; top: 178px;
    font: 400 16px "Lato", sans-serif; color: var(--ink);
  }
  .service-right {
    left: 425px; top: 178px;
    font: 400 18px "Lato", sans-serif; color: var(--ink);
  }
  .address {
    left: 25px; top: 223px;
    font: 400 13px "Roboto Condensed", sans-serif; color: var(--ink);
    line-height: 18px; white-space: normal; width: 140px;
  }
  .phone {
    left: 277px; top: 230px;
    font: 700 29px "Roboto Condensed", sans-serif; color: var(--ink);
  }
  .experience {
    left: 483px; top: 223px;
    font: 400 13px "Roboto Condensed", sans-serif; color: var(--ink);
    line-height: 18px; text-align: center;
  }
  .open-days {
    left: 277px; top: 299px;
    font: 700 23px "Open Sans", sans-serif; color: var(--white);
  }

  .back-header {
    position: absolute; left: 0; top: 0; width: 100%; height: 107px;
    background: var(--teal);
  }
  .appt-title {
    left: 279px; top: 22px;
    font: 400 25px "Lato", sans-serif; color: var(--white);
  }
  .appt-vet {
    left: 279px; top: 51px;
    font: 400 20px "Tinos", serif; color: var(--white);
  }
  .appt-phone {
    left: 279px; top: 75px;
    font: 400 17px "Lato", sans-serif; color: var(--white);
  }
  .appt-line {
    font: 400 18px "Lato", sans-serif; color: var(--grey);
  }
  .appt-for { left: 48px; top: 172px; }
  .appt-when { left: 45px; top: 230px; }
  .weekdays {
    position: absolute; left: 47px; top: 276px;
    display: flex; gap: 20px;
    font: 400 17px "Lato", sans-serif; color: var(--grey);
  }
  .weekday { display: flex; align-items: center; gap: 5px; }
  .checkbox {
    width: 20px; height: 20px;
    border: 1.5px solid var(--grey); background: var(--white);
  }
</style>
</head>
<body>

<section class="card card-front" aria-label="Business card front">
  <svg class="bands" width="555" height="343" viewBox="0 0 555 343" aria-hidden="true">
    <rect x="0" y="0" width="555" height="84" fill="var(--teal)"/>
    <polygon points="0,53 555,74 555,84 0,84" fill="var(--black)"/>
    <rect x="0" y="280" width="555" height="63" fill="var(--teal)"/>
    <polygon points="0,280 555,280 555,310 0,290" fill="var(--black)"/>
  </svg>

  <h1 class="txt center hospital-name">Fenbrook Hollow Animal Hospital</h1>
  <p class="txt center vet-name">Gregory L.&nbsp; Ashworth ,DVM</p>
  <p class="txt center website">www.fenbrookhollowanimalhospital.example</p>
  <p class="txt service-left">Emergency Services</p>
  <p class="txt center species">Cats &#9679; Dogs &nbsp;&#9679; &nbsp;Birds &#9679; Exotics</p>
  <p class="txt service-right">House Calls</p>
  <p class="txt address">1873 Tilden Marsh Rd Loveland, OH 45140</p>
  <p class="txt center phone">(513) 555-0148</p>
  <p class="txt center experience">38 years of<br>experience</p>
  <p class="txt center open-days">OPEN 7 DAYS A WEEK</p>
</section>

<section class="card card-back" aria-label="Business card back">
  <div class="back-header"></div>
  <h2 class="txt center appt-title">Veterinary Appointment</h2>
  <p class="txt center appt-vet">Gregory L.Ashworth, DVM</p>
  <p class="txt center appt-phone">513.555.0148</p>

  <p class="txt appt-line appt-for">YOUR APPOINTMENT FOR .......................................IS ON</p>
  <p class="txt appt-line appt-when">Date : ................................&nbsp;&nbsp; Time : ............................. AM / PM</p>
  <div class="weekdays">
    <span class="weekday"><span class="checkbox"></span>MON</span>
    <span class="weekday"><span class="checkbox"></span>TUE</span>
    <span class="weekday"><span class="checkbox"></span>WED</span>
    <span class="weekday"><span class="checkbox"></span>THU</span>
    <span class="weekday"><span class="checkbox"></span>FRI</span>
    <span class="weekday"><span class="checkbox"></span>SAT</span>
  </div>
</section>

</body>
</html>
```